Website redesign for a national printing company

Our current website is dated and boring: tidewellflags.com

We are looking for a fresh, modern design. We need a clean, minimal design that is also elegant, really shows off large, bright photos of our banners in action and POPS. Our goal is to showcase our beautiful banners, while also giving the user the confidence in our company that we will provide friendly, fast service, fast printing, and deliver their banners on time for their event.

I want a nice flow to the website, the design should tie in well with the printing feel. Here is an example of clean, beautiful design that ties in to the industry - https://www.vorpa.com/ - notice how the buttons are like chat icons, for example.

More examples:

Nice clean design https://www.brimlet.com/

https://quelmoor.com/ nice and clean, but it POPS really well.

I like https://www.fendrawick.com/

https://www.pruvel.com/ gorgeous site, clean, modern

Beautiful, simple, clean, modern - https://tanvirepay.com/en-us/

These websites are not from the print industry, that’s because most printers don’t have good websites - they are more focused on local businesses, referrals, not really online marketing.

But keep in mind in your design that we need to give the feel that we are printing their banners beautifully, fast, with great service.

https://www.gleamvoxa.com/ so clean, bold, clear to the user what the company does. Love this simple yet elegant design.

https://www.k7.com/ - so pretty! And still so simple and obvious to the user what to do on their site.

https://zelvin.com/

https://marrowfinch.com/us/en/ big and bold - yet super nicely designed with so many nice touches

https://postwrenly.com/ - also clean, simple, and so obvious to the user to take action and contact the company
Updates

I just updated the job brief, and you can also view it in full here - https://files.qorvanet.com/document/d/8Hpz3LRQx-41mTb92nWvJcOaEs-Y67kd0Gf57JuXRTNe/edit?usp=sharing

Target Market(s)

Please read this customer persona - https://files.qorvanet.com/document/d/8Hpz3LRQx-41mTb92nWvJcOaEs-Y67kd0Gf57JuXRTNe/edit?usp=sharing

Industry/Entity Type

Printing

Number of Pages Required

1 page

Requirements
Must have
• Nice flow to the website, the design should tie in well with the printing feel. Here is an example of clean, beautiful design that ties in to the industry - https://www.vorpa.com/ - notice how the buttons are like chat icons, for example.
Should not have
• No filters on the images, we want large, beautiful images.

```html
<!DOCTYPE html>
<html lang="en">
<head>
<meta charset="utf-8">
<title>Tidewell Flags — Fast, Flexible, Friendly Banner Printing</title>
<link rel="stylesheet" href="https://fonts.googleapis.com/css2?family=Poppins:wght@400;500;600;700&display=swap">
<style>
:root{
  --blue:#1d4ed2;
  --blue-deep:#1639a8;
  --blue-bright:#2a63e6;
  --ink:#111318;
  --text:#4a4f5c;
  --muted:#8a90a0;
  --mist:#e9edf6;
  --white:#ffffff;
  --star:#f5b301;
}
*{box-sizing:border-box;margin:0;padding:0}
html,body{width:1200px;height:4549px;overflow:hidden}
body{font-family:"Poppins",sans-serif;color:var(--ink);background:var(--white);position:relative}
.abs{position:absolute}
.btn{position:absolute;display:flex;align-items:center;justify-content:center;font-size:15px;font-weight:600;letter-spacing:.2px;text-transform:uppercase;color:var(--white);background:var(--blue);border-radius:12px 12px 12px 2px;text-decoration:none}
.btn-outline{background:transparent;border:1.5px solid currentColor;border-radius:12px 12px 12px 2px}

/* hero */
.hero-bg{left:0;top:0;width:1200px;height:720px;background:linear-gradient(160deg,var(--blue-bright) 0%,var(--blue) 45%,var(--blue-deep) 100%);clip-path:polygon(0 0,100% 0,100% 600px,0 715px)}
.hero-stripe{background:rgba(255,255,255,.06)}
.corner-white{right:0;top:600px;width:340px;height:120px;background:var(--mist);clip-path:polygon(100% 0,100% 100%,0 100%)}
.brand{font-weight:600;color:var(--white);line-height:1}
.brand .name{font-size:28px;display:block}
.brand .tag{font-size:11px;letter-spacing:7px;display:block;margin-top:4px;padding-left:40px}
.nav{font-size:13px;color:var(--white)}
.nav span{position:absolute;white-space:nowrap}
.tollfree{left:732px;top:25px;color:var(--white);display:flex;gap:10px;align-items:center}
.tollfree small{display:block;font-size:11px}
.tollfree b{font-size:15px;font-weight:600}
.btn-head{border:1.5px solid rgba(255,255,255,.6);font-size:14px;height:39px;top:23px;background:var(--blue)}
.hero-title{left:0;top:152px;width:1200px;text-align:center;color:var(--white);font-size:48px;font-weight:600;line-height:56px}
.hero-sub{left:0;top:278px;width:1200px;text-align:center;color:var(--white);font-size:14.5px}
.slide{left:224px;top:365px;width:750px;height:412px;background:linear-gradient(180deg,#c9ced6 0%,#aeb6c2 35%,#3c4656 60%,#6f7680 82%,#d8dbe0 100%)}
.slide-arrow{width:42px;height:42px;border-radius:50%;background:var(--white);border:2px solid var(--blue);display:flex;align-items:center;justify-content:center;top:545px}
.slide-caption{left:450px;top:699px;width:297px;height:42px;border-radius:21px;background:rgba(22,40,110,.85);color:var(--white);font-size:19px;font-weight:500;display:flex;align-items:center;justify-content:center}
.rating{left:0;top:814px;width:1200px;display:flex;justify-content:center;align-items:center;gap:12px;font-size:13px;color:var(--ink)}
.rating .stars{color:var(--star);font-size:20px;letter-spacing:2px;line-height:1}
.rating .src{display:flex;align-items:center;gap:6px;font-weight:600;font-size:15px}
.rating .src i{width:12px;height:12px;border-radius:50%;background:var(--blue);display:block}

/* section heads */
.eyebrow{left:0;width:1200px;text-align:center;color:var(--blue);font-size:17px}
.heading{left:0;width:1200px;text-align:center;font-size:36px;font-weight:600;line-height:46px}
.heading em{font-style:normal;color:var(--blue)}

/* products */
.product{width:220px;text-align:center;top:1083px}
.product .pic{width:134px;height:134px;border-radius:50%;margin:0 auto}
.product p{margin-top:34px;font-size:17px;font-weight:500}
.product.active p{color:var(--blue)}

/* feature */
.feature-title{left:129px;top:1356px;font-size:38px;font-weight:600;line-height:40px}
.feature-title em{font-style:normal;color:var(--blue)}
.feature-copy{left:129px;top:1451px;width:415px;font-size:12.5px;line-height:25.5px;color:var(--text)}
.collage{left:605px;top:1336px}

/* band */
.band-bg{left:0;top:1721px;width:1200px;height:556px;background:var(--mist);clip-path:polygon(0 92px,100% 0,100% 464px,0 556px)}
.band-photo{left:139px;top:1866px;width:484px;height:287px;border-radius:10px;background:linear-gradient(100deg,#1c1a18 0%,#5a4530 35%,#3a3430 55%,#8a5a2c 75%,#c98a3e 100%)}
.quote-bubble{left:85px;top:1984px;width:198px;height:198px;border-radius:50%;background:var(--white);box-shadow:0 8px 24px rgba(0,0,0,.12);text-align:center;padding-top:40px}
.quote-bubble .stars{color:var(--star);font-size:19px;letter-spacing:3px}
.quote-bubble p{font-size:12.5px;line-height:19px;color:var(--ink);margin:6px 20px 0}
.quote-bubble b{display:block;color:var(--blue);font-size:13.5px;font-weight:600;margin-top:14px}
.band-title{left:692px;top:1900px;font-size:36px;font-weight:600}
.band-title em{font-style:normal;color:var(--blue)}
.band-copy{left:692px;top:1951px;width:370px;font-size:14px;line-height:23px;color:var(--text)}

/* process */
.process-bg{left:0;top:2185px;width:1200px;height:760px;background:linear-gradient(170deg,var(--blue-bright),var(--blue) 50%,var(--blue-deep));clip-path:polygon(0 92px,100% 0,100% 759px,0 666px)}
.process-fade{left:0;top:2500px;width:520px;height:300px;background:radial-gradient(ellipse at 30% 50%,rgba(255,255,255,.07),transparent 70%)}
.step-icon{width:96px;height:96px;border-radius:50%;background:var(--white);display:flex;align-items:center;justify-content:center;box-shadow:0 6px 18px rgba(0,0,0,.18)}
.step-num{width:24px;height:24px;border-radius:50%;background:rgba(255,255,255,.85);color:var(--blue);font-size:12px;font-weight:600;display:flex;align-items:center;justify-content:center}
.step-label{color:var(--white);font-size:15px;line-height:23px;font-weight:500}
.center-mark{left:462px;top:2439px;width:276px;height:276px;display:flex;align-items:center;justify-content:center;color:var(--white);font-size:32px;font-weight:600;text-align:center;line-height:38px}

/* testimonials */
.intro{left:0;top:3113px;width:1200px;text-align:center;font-size:15px;line-height:26px;color:var(--text)}
.review-card{left:139px;top:3209px;width:922px;height:420px;border-radius:12px;background:var(--white);box-shadow:0 8px 30px rgba(20,40,100,.10);overflow:hidden}
.review-photo{left:472px;top:0;width:450px;height:420px;background:linear-gradient(120deg,#141414 0%,#2b2b2e 40%,#8a8230 65%,#2a2a2d 80%,#0f0f10 100%)}
.avatar{left:52px;top:46px;width:84px;height:84px;border-radius:50%;background:linear-gradient(160deg,#d8b48c,#9a6b48)}
.review-stars{left:50px;top:140px;color:var(--star);font-size:20px;letter-spacing:3px}
.review-name{left:51px;top:178px;font-size:17px;font-weight:600;color:var(--blue)}
.review-when{left:51px;top:205px;font-size:10.5px;color:var(--muted)}
.review-text{left:51px;top:240px;width:370px;font-size:14px;line-height:26px;color:var(--text)}
.logos{left:0;top:3780px;width:1200px;height:50px}
.logo-word{position:absolute;top:12px;transform:translateX(-50%);font-size:22px;font-weight:600;color:#3a5fc8;white-space:nowrap}

/* cta */
.cta-bg{left:0;top:3892px;width:1200px;height:380px;background:var(--mist);clip-path:polygon(0 88px,100% 0,100% 290px,0 380px)}
.cta-mark{left:213px;top:4010px;width:76px;height:90px;background:var(--blue)}
.cta-title{left:314px;top:4018px;font-size:38px;font-weight:600;line-height:48px;color:var(--blue)}

/* footer */
.footer-bg{left:0;top:4183px;width:1200px;height:366px;background:linear-gradient(170deg,var(--blue-bright),var(--blue) 50%,var(--blue-deep));clip-path:polygon(0 71px,100% 0,100% 100%,0 100%)}
.foot-col{color:var(--white)}
.foot-col h4{font-size:16px;font-weight:500;margin-bottom:16px}
.foot-col li{list-style:none;font-size:12px;line-height:27px}
.social{width:40px;height:40px;border-radius:50%;border:1.5px solid var(--white);top:4373px}
.social.solid{background:var(--white)}
.rule{left:60px;top:4494px;width:1080px;height:1px;background:rgba(255,255,255,.3)}
.copyright{left:60px;top:4513px;font-size:11.5px;color:var(--white)}
.bottom-links{left:830px;top:4511px;font-size:13.5px;font-weight:600;color:var(--white);white-space:nowrap}
</style>
</head>
<body>

<!-- hero -->
<div class="abs hero-bg"></div>
<div class="abs hero-stripe" style="left:0;top:0;width:1200px;height:720px;clip-path:polygon(0 120px,420px 0,560px 0,0 360px)"></div>
<div class="abs hero-stripe" style="left:0;top:0;width:1200px;height:720px;clip-path:polygon(1000px 0,1200px 0,1200px 140px,820px 600px,700px 640px)"></div>
<div class="abs corner-white"></div>

<div class="abs brand" style="left:58px;top:21px"><span class="name">Tidewell Flags</span><span class="tag">BANNERS</span></div>
<nav class="abs nav" style="left:0;top:33px;width:1200px">
  <span style="left:300px">About</span>
  <span style="left:360px">Products&nbsp;⌄</span>
  <span style="left:455px">Galleries&nbsp;⌄</span>
  <span style="left:552px">Contact Us</span>
</nav>
<div class="abs tollfree">
  <svg width="26" height="26" viewBox="0 0 24 24" fill="none" stroke="#fff" stroke-width="1.6"><path d="M5 3h4l2 5-3 2a12 12 0 0 0 6 6l2-3 5 2v4a2 2 0 0 1-2 2A18 18 0 0 1 3 5a2 2 0 0 1 2-2z"/></svg>
  <div><small>Toll Free</small><b>800-555-0142</b></div>
</div>
<a class="btn btn-head" style="left:895px;width:95px">Upload</a>
<a class="btn btn-head" style="left:1006px;width:132px">Get a Quote</a>

<h1 class="abs hero-title">Fast, Flexible, Friendly Deliver<br>Your Banners</h1>
<p class="abs hero-sub">We Will Provide Friendly, Fast Service, Fast Printing, And Deliver Their Banners On Time For Their Event.</p>
<a class="btn btn-outline" style="left:531px;top:314px;width:136px;height:41px;color:var(--white);font-size:14px">Get a Quote</a>

<div class="abs slide" role="img" aria-label="Outdoor festival stage framed by large printed plastic roll banners"></div>
<div class="abs slide-arrow" style="left:203px"><svg width="14" height="14" viewBox="0 0 14 14"><path d="M9 2 4 7l5 5" fill="none" stroke="#1d4ed2" stroke-width="2"/></svg></div>
<div class="abs slide-arrow" style="left:953px"><svg width="14" height="14" viewBox="0 0 14 14"><path d="m5 2 5 5-5 5" fill="none" stroke="#1d4ed2" stroke-width="2"/></svg></div>
<div class="abs slide-caption">Plastic Roll Banners</div>

<div class="abs rating">
  <span>Excellent</span>
  <span class="stars">★★★★★</span>
  <span>44 Reviews on</span>
  <span class="src"><i></i>Gleamvoxa</span>
</div>

<!-- products -->
<p class="abs eyebrow" style="top:916px">Our Products</p>
<h2 class="abs heading" style="top:950px">We Provide The On Time<br><em>Printing Services</em></h2>
<div class="abs product active" style="left:273px"><div class="pic" role="img" aria-label="Team holding a printed sponsor banner" style="background:linear-gradient(150deg,#c7ccd4,#8a3a3a 55%,#2f3a58)"></div><p>Marketing Manager</p></div>
<div class="abs product" style="left:490px"><div class="pic" role="img" aria-label="Festival stage at dusk with banners" style="background:linear-gradient(180deg,#8fa7e0,#d89aa8 40%,#3a4a7a 70%,#7a5b40)"></div><p>Festival Producer</p></div>
<div class="abs product" style="left:707px"><div class="pic" role="img" aria-label="Stadium wall wrapped in a large mesh banner" style="background:linear-gradient(180deg,#3a5db5,#1c2f6a 60%,#0f1c44)"></div><p>Large&amp; Mesh Banner</p></div>

<!-- plastic roll feature -->
<h2 class="abs feature-title">Plastic Roll<br><em>Banners</em></h2>
<p class="abs feature-copy">Plastic Roll Banners offer an economical and effective way to communicate your marketing message at concerts, sporting events, radio station events, motor sports events, political rallies, and anywhere else groups of people gather. Printed on 4 mil or 6 mil low density polyethylene, they are easily recyclable and biodegradable.</p>
<a class="btn" style="left:129px;top:1624px;width:157px;height:41px">Learn More</a>

<svg class="abs collage" width="450" height="318" viewBox="0 0 450 318" role="img" aria-label="Gallery of plastic roll banners at events">
  <defs>
    <linearGradient id="t1" x1="0" y1="0" x2="1" y2="1"><stop offset="0" stop-color="#c33a3a"/><stop offset="1" stop-color="#2b3550"/></linearGradient>
    <linearGradient id="t2" x1="0" y1="0" x2="1" y2="1"><stop offset="0" stop-color="#3a3f4a"/><stop offset="1" stop-color="#b8bcc6"/></linearGradient>
    <linearGradient id="t3" x1="0" y1="0" x2="1" y2="1"><stop offset="0" stop-color="#9fb2d6"/><stop offset="1" stop-color="#8a4a3a"/></linearGradient>
    <linearGradient id="t4" x1="0" y1="0" x2="1" y2="1"><stop offset="0" stop-color="#6e8fc8"/><stop offset="1" stop-color="#3d5a2e"/></linearGradient>
    <linearGradient id="t5" x1="0" y1="0" x2="1" y2="1"><stop offset="0" stop-color="#b23030"/><stop offset="1" stop-color="#1f2a44"/></linearGradient>
    <linearGradient id="t6" x1="0" y1="0" x2="1" y2="1"><stop offset="0" stop-color="#c8cdd6"/><stop offset="1" stop-color="#2a2f3c"/></linearGradient>
    <linearGradient id="t7" x1="0" y1="0" x2="1" y2="1"><stop offset="0" stop-color="#e6e8ec"/><stop offset="1" stop-color="#4a79c8"/></linearGradient>
    <linearGradient id="t8" x1="0" y1="0" x2="1" y2="1"><stop offset="0" stop-color="#1f5a3a"/><stop offset="1" stop-color="#d8d2b8"/></linearGradient>
    <linearGradient id="t9" x1="0" y1="0" x2="1" y2="1"><stop offset="0" stop-color="#3a3a3a"/><stop offset="1" stop-color="#e0ddd4"/></linearGradient>
  </defs>
  <polygon points="0,0 106,0 160,98 54,98" fill="url(#t1)"/>
  <polygon points="110,0 216,0 270,98 164,98" fill="url(#t2)"/>
  <polygon points="220,0 326,0 380,98 274,98" fill="url(#t3)"/>
  <polygon points="48,108 154,108 208,206 102,206" fill="url(#t4)"/>
  <polygon points="158,108 264,108 318,206 212,206" fill="url(#t5)"/>
  <polygon points="268,108 374,108 428,206 322,206" fill="url(#t6)"/>
  <polygon points="92,216 198,216 250,318 144,318" fill="url(#t7)"/>
  <polygon points="202,216 308,216 360,318 254,318" fill="url(#t8)"/>
  <polygon points="312,216 398,216 450,318 364,318" fill="url(#t9)"/>
</svg>

<!-- band -->
<div class="abs band-bg"></div>
<div class="abs band-photo" role="img" aria-label="Musician on stage in front of a custom printed backdrop"></div>
<div class="abs quote-bubble">
  <div class="stars">★★★★★</div>
  <p>"Fantastic product. Good quality. Fast and friendly service"</p>
  <b>Dalton Reeve</b>
</div>
<h2 class="abs band-title">Are You <em>a Band?</em></h2>
<p class="abs band-copy">Contact our product experts for all your pricing and sizing needs.</p>
<a class="btn" style="left:692px;top:2025px;width:288px;height:42px">stagecloths.com</a>

<!-- process -->
<div class="abs process-bg"></div>
<div class="abs process-fade"></div>
<p class="abs eyebrow" style="top:2307px;color:var(--white);font-size:16px">How It Work</p>
<h2 class="abs heading" style="top:2346px;color:var(--white)">Our Process Is<br>Fast And Simple</h2>

<svg class="abs" style="left:440px;top:2417px" width="320" height="310" viewBox="0 0 320 310" aria-hidden="true">
  <path d="M54 88 A138 138 0 1 0 266 88" fill="none" stroke="rgba(255,255,255,.85)" stroke-width="1.6"/>
  <circle cx="54" cy="88" r="3" fill="#fff"/><circle cx="266" cy="88" r="3" fill="#fff"/>
</svg>
<div class="abs center-mark">Tidewell<br>Flags</div>

<div class="abs step-icon" style="left:374px;top:2495px">
  <svg width="44" height="44" viewBox="0 0 44 44" fill="none" stroke="#1d4ed2" stroke-width="2.2"><rect x="8" y="8" width="28" height="22" rx="2"/><path d="M4 34h36"/><path d="M22 25V14m-5 5 5-5 5 5"/></svg>
</div>
<div class="abs step-icon" style="left:729px;top:2495px">
  <svg width="44" height="44" viewBox="0 0 44 44" fill="none" stroke="#1d4ed2" stroke-width="2.2"><rect x="6" y="14" width="32" height="16" rx="2"/><path d="M12 14V6h20v8M12 30v8h20v-8"/><circle cx="33" cy="19" r="1.5" fill="#1d4ed2"/></svg>
</div>
<div class="abs step-icon" style="left:420px;top:2661px">
  <svg width="44" height="44" viewBox="0 0 44 44" fill="none" stroke="#1d4ed2" stroke-width="2.2"><rect x="7" y="12" width="30" height="20" rx="2" transform="rotate(-15 22 22)"/><path d="m9 16 13 9 13-9" transform="rotate(-15 22 22)"/></svg>
</div>
<div class="abs step-icon" style="left:681px;top:2661px">
  <svg width="44" height="44" viewBox="0 0 44 44" fill="none" stroke="#1d4ed2" stroke-width="2.2"><rect x="6" y="16" width="32" height="20" rx="3"/><path d="M6 23h32M11 30h6"/><circle cx="30" cy="12" r="7" fill="#fff"/><path d="m27 12 2 2 4-4"/></svg>
</div>

<div class="abs step-num" style="left:336px;top:2515px">1</div>
<div class="abs step-num" style="left:844px;top:2500px">4</div>
<div class="abs step-num" style="left:375px;top:2669px">2</div>
<div class="abs step-num" style="left:800px;top:2669px">3</div>

<p class="abs step-label" style="left:197px;top:2545px;width:160px;text-align:right">Upload Art Files</p>
<p class="abs step-label" style="left:849px;top:2529px">You're done!<br>We Start Printing</p>
<p class="abs step-label" style="left:214px;top:2701px;width:180px;text-align:right">Receive A Proof<br>In Your Inbox</p>
<p class="abs step-label" style="left:800px;top:2701px">Approve The Proof<br>And Make Payment</p>

<a class="btn btn-outline" style="left:531px;top:2780px;width:136px;height:41px;color:var(--white);font-size:14px">Get a Quote</a>

<!-- testimonials -->
<p class="abs eyebrow" style="top:2985px;font-size:16px">Testimonials</p>
<h2 class="abs heading" style="top:3020px">Rated 5/5 Stars By Our<br><em>Customers</em></h2>
<p class="abs intro">Read our Searchly reviews and see why radio stations, festival organizers, bands and<br>many other companies love Tidewell Flags.</p>

<div class="abs review-card">
  <div class="abs avatar" role="img" aria-label="Reviewer portrait"></div>
  <div class="abs review-stars">★★★★★</div>
  <p class="abs review-name">Corinne Vale</p>
  <p class="abs review-when">1 month ago</p>
  <p class="abs review-text">The banner turned out great and was delivered promptly. Looks great at gigs. Corinne Vale, Rusty Lane and the Night Owls</p>
  <svg class="abs" style="left:44px;top:362px" width="120" height="32" viewBox="0 0 120 32" aria-hidden="true">
    <circle cx="16" cy="16" r="15" fill="#1d4ed2"/><path d="m19 10-6 6 6 6" fill="none" stroke="#fff" stroke-width="2"/>
    <path d="M38 16h62" stroke="#1d4ed2" stroke-width="1.5" stroke-dasharray="3 4"/><path d="m100 11 6 5-6 5" fill="none" stroke="#1d4ed2" stroke-width="2"/>
  </svg>
  <div class="abs review-photo" role="img" aria-label="Band members posing in front of their printed stage banner"></div>
</div>

<h3 class="abs heading" style="top:3708px;font-size:26px;font-weight:500">As Seen In</h3>
<div class="abs logos">
  <span class="logo-word" style="left:138px">Orbit TV</span>
  <span class="logo-word" style="left:323px">Harbor Comets</span>
  <span class="logo-word" style="left:508px">Pulsewave</span>
  <span class="logo-word" style="left:687px">Crestline</span>
  <span class="logo-word" style="left:870px">Altostrat</span>
  <span class="logo-word" style="left:1052px">Boroughline</span>
</div>

<!-- call to action -->
<div class="abs cta-bg"></div>
<div class="abs cta-mark" aria-hidden="true"></div>
<h2 class="abs cta-title">Drop Us A Line, We'd<br>Love to Help !</h2>
<a class="btn" style="left:828px;top:4028px;width:157px;height:41px">Get a Quote</a>

<!-- footer -->
<footer>
  <div class="abs footer-bg"></div>
  <div class="abs brand" style="left:88px;top:4306px"><span class="name" style="font-size:30px">Tidewell Flags</span><span class="tag" style="padding-left:44px">BANNERS</span></div>
  <div class="abs social solid" style="left:114px"></div>
  <div class="abs social" style="left:162px"></div>
  <div class="abs social" style="left:209px"></div>

  <div class="abs foot-col" style="left:337px;top:4277px">
    <h4>Quick Links</h4>
    <ul><li>Request a Catalog</li><li>Blogs</li><li>Articles</li><li>FAQ</li><li>stagecloths.com</li></ul>
  </div>
  <div class="abs foot-col" style="left:612px;top:4277px">
    <h4>Quick Links</h4>
    <ul><li>Customer Reviews</li><li>Customer Sales Contract</li><li>Privacy Policy</li></ul>
  </div>
  <div class="abs foot-col" style="left:886px;top:4277px">
    <h4>Contact Us</h4>
  </div>
  <svg class="abs" style="left:884px;top:4318px" width="28" height="28" viewBox="0 0 24 24" fill="none" stroke="#fff" stroke-width="1.5"><path d="M5 3h4l2 5-3 2a12 12 0 0 0 6 6l2-3 5 2v4a2 2 0 0 1-2 2A18 18 0 0 1 3 5a2 2 0 0 1 2-2z"/></svg>
  <div class="abs foot-col" style="left:925px;top:4316px;font-size:14px;line-height:24px">800-555-0142<br>734-555-0187<br><small style="font-size:10.5px">(Local and Canada)</small></div>
  <svg class="abs" style="left:884px;top:4401px" width="28" height="22" viewBox="0 0 28 22" fill="none" stroke="#fff" stroke-width="1.5"><rect x="1" y="1" width="26" height="20" rx="2"/><path d="m1 2 13 10L27 2"/></svg>
  <div class="abs foot-col" style="left:925px;top:4402px;font-size:13.5px">info@tidewellflags.com</div>

  <div class="abs rule"></div>
  <p class="abs copyright">©Tidewell Flags – 2023 All rights reserved.</p>
  <p class="abs bottom-links">Get a Quote &nbsp;|&nbsp; Upload &nbsp;|&nbsp; Contact Us &nbsp;|&nbsp; Pay</p>
</footer>

</body>
</html>
```